Business Card Design

I need a business card design for a new company that is based in Singapore region. The name of the company is called " Tarsuki Holdings Pte.Ltd " This company serves as a holding company that owns several types of businesses under our name. One of the established company in Singapore is the Tarsuki Food Industries that serves as a food service industry that has their own brand name which operates in malls and CBD areas. We would prefer the design of the business cards will use the colors of black as the base and red as for the designs. The final design of the name card should be able to communicate young and professional type of business culture. In which we appreciate creativity to their highest point.
Updates
Industry/Entity Type
Industry
Contact Information for Business Card
Morell Castian Tarsuki
Director, Founder
Contact: +65 91472630
E-mail: morellct@quenmail.com
Look and feel

```html
<!DOCTYPE html>
<html lang="en">
<head>
<meta charset="UTF-8">
<title>Tarsuki Holdings – Business Card</title>
<link rel="stylesheet" href="https://fonts.googleapis.com/css2?family=Exo+2:ital,wght@0,400;0,600;1,400&family=Open+Sans:wght@400;600&display=swap">
<style>
  :root {
    --bg: #8a8a8a;
    --card-white: #f4f4f3;
    --card-black: #141414;
    --red: #e0392b;
    --ink: #3a3a3a;
    --faint-light: #e4e4e3;
    --faint-dark: #1d1d1d;
    --grey-text: #555555;
  }
  * { box-sizing: border-box; margin: 0; padding: 0; }
  html, body { width: 1200px; height: 1000px; overflow: hidden; }
  body {
    background: var(--bg);
    position: relative;
    font-family: "Open Sans", sans-serif;
  }
  .card {
    position: absolute;
    left: 280px;
    width: 640px;
    height: 384px;
    border-radius: 4px;
    overflow: hidden;
    box-shadow: 0 10px 28px rgba(0,0,0,.35);
  }

  /* ---------- Back side ---------- */
  .card-back { top: 70px; background: var(--card-black); }
  .card-back .backdrop-ring {
    position: absolute; left: 180px; top: 52px;
    width: 280px; height: 280px; border-radius: 50%;
    border: 26px solid var(--faint-dark);
  }
  .card-back .brand {
    position: absolute; left: 0; right: 0; top: 118px;
    display: flex; flex-direction: column; align-items: center; gap: 14px;
  }
  .card-back .brand-ring {
    width: 74px; height: 74px; border-radius: 50%;
    border: 5px solid var(--red);
  }
  .card-back .brand-name {
    font-family: "Exo 2", sans-serif; font-weight: 600;
    font-size: 30px; letter-spacing: 2px; text-transform: uppercase;
    color: var(--red);
  }

  /* ---------- Front side ---------- */
  .card-front { top: 530px; background: var(--card-white); }
  .card-front .backdrop-ring {
    position: absolute; left: 360px; top: 190px;
    width: 260px; height: 260px; border-radius: 50%;
    border: 22px solid var(--faint-light);
  }
  .card-front .corner-brand {
    position: absolute; right: 30px; top: 30px;
    display: flex; flex-direction: column; align-items: center; gap: 5px;
  }
  .card-front .brand-ring {
    width: 30px; height: 30px; border-radius: 50%;
    border: 2.5px solid var(--red);
  }
  .card-front .brand-name {
    font-family: "Exo 2", sans-serif; font-weight: 600;
    font-size: 12px; letter-spacing: .8px; text-transform: uppercase;
    color: var(--red);
  }
  .name-band {
    position: absolute; left: 0; top: 136px;
    width: 150px; height: 10px; background: var(--red);
  }
  .name-tab {
    position: absolute; left: 140px; top: 126px;
    width: 300px; height: 32px; border-radius: 6px;
    background: var(--red);
    display: flex; align-items: center; justify-content: center;
  }
  .person-name {
    font-family: "Exo 2", sans-serif; font-style: italic; font-weight: 400;
    font-size: 22px; color: #fff; letter-spacing: .3px;
  }
  .person-title {
    position: absolute; left: 140px; width: 300px; top: 168px;
    text-align: center;
    font-family: "Exo 2", sans-serif; font-size: 16px; color: var(--ink);
  }
  .contact {
    position: absolute; left: 458px; top: 160px;
    display: flex; gap: 10px; align-items: stretch;
  }
  .contact .divider { width: 2px; background: var(--red); }
  .contact ul { list-style: none; display: flex; flex-direction: column; gap: 4px; }
  .contact li {
    display: flex; align-items: center; gap: 6px;
    font-size: 11px; color: var(--ink);
  }
  .contact svg { width: 11px; height: 11px; fill: var(--red); }
</style>
</head>
<body>

  <section class="card card-back" aria-label="Business card back">
    <div class="backdrop-ring"></div>
    <div class="brand">
      <div class="brand-ring"></div>
      <div class="brand-name">Tarsuki Holdings</div>
    </div>
  </section>

  <section class="card card-front" aria-label="Business card front">
    <div class="backdrop-ring"></div>

    <div class="corner-brand">
      <div class="brand-ring"></div>
      <div class="brand-name">Tarsuki Holdings</div>
    </div>

    <div class="name-band"></div>
    <div class="name-tab"><span class="person-name">Morell Castian Tarsuki</span></div>
    <p class="person-title">Director, Founder</p>

    <div class="contact">
      <span class="divider"></span>
      <ul>
        <li>
          <svg viewBox="0 0 24 24" aria-hidden="true"><path d="M6.6 10.8a15 15 0 0 0 6.6 6.6l2.2-2.2a1 1 0 0 1 1-.25 11.4 11.4 0 0 0 3.6.57 1 1 0 0 1 1 1V20a1 1 0 0 1-1 1A17 17 0 0 1 3 4a1 1 0 0 1 1-1h3.5a1 1 0 0 1 1 1c0 1.25.2 2.45.57 3.57a1 1 0 0 1-.25 1z"/></svg>
          <span>+65 91472630</span>
        </li>
        <li>
          <svg viewBox="0 0 24 24" aria-hidden="true"><path d="M2 5h20v14H2z M2 5l10 8 10-8" /></svg>
          <span>morellct@quenmail.com</span>
        </li>
      </ul>
    </div>
  </section>

</body>
</html>
```